Brivolo Brochure

I need to create the first collateral material for the launch of my new Tech Startup called Brivolo. I will need to develop a Brochure that states the description of the company and it products. I Have the Brivvolo logo in PSD and a preliminary brochure in power Point

Target Market(s)

APP, Game Developers, Advertising Agencies and Brands

Requirements
Must have
• It needs to be a brochure with a contemporary look. The colors are in the PSD provided. Some images in the PPT Provided might change a bit such as the dashboard layouts. Notice that the logo there is not the official one. USE ONLY THE BRIVOLO LOGO. NOT THE TALLERES DE MIEL logos.
Nice to have
• Clean design. Modern and readable fonts

```html
<!DOCTYPE html>
<html lang="es">
<head>
<meta charset="utf-8">
<title>Brivolo – Folleto</title>
<link rel="stylesheet" href="https://fonts.googleapis.com/css2?family=Lato:wght@400;700;900&family=Dancing+Script:wght@500&display=swap">
<style>
  :root{
    --stage:#e6e4e1;
    --brand-red:#c23d2c;
    --inside-red:#c4492f;
    --deep-red:#8d1f17;
    --spine:#1a1210;
    --accent:#f6a53a;
    --ink-dark:#3b1913;
    --ink-light:#ffffff;
    --photo-light:#eef4f8;
    --photo-blue:#a9c4d6;
    --device:#1c1c1e;
  }
  *{box-sizing:border-box;margin:0;padding:0}
  html,body{width:1200px;height:910px;overflow:hidden}
  body{background:var(--stage);font-family:"Lato",Arial,sans-serif;position:relative}

  .page{position:absolute;top:126px;height:667px;overflow:hidden}
  .page--front{left:88px;width:478px;background:var(--brand-red);border-left:5px solid var(--spine)}
  .page--inside{left:638px;width:475px;background:var(--inside-red);border-left:4px solid var(--spine)}
  .page--inside::after{content:"";position:absolute;left:5px;top:0;bottom:0;width:1px;background:var(--spine);opacity:.7}

  .cover-art{position:absolute;left:0;top:0}
  .device-shot{position:absolute;left:244px;top:50px;width:193px;height:414px;border-radius:28px;
    background:linear-gradient(160deg,#3a3a3c,var(--device) 40%,#0c0c0d)}
  .device-shot::before{content:"";position:absolute;left:14px;right:14px;top:62px;bottom:62px;
    background:linear-gradient(180deg,#f3a23a 0 6%,#f4f4f4 6% 88%,#2a2a2a 88%)}

  .brand{position:absolute;left:58px;top:392px;display:flex;align-items:center;gap:10px}
  .brand__dot{width:22px;height:22px;border-radius:50%;background:var(--spine)}
  .brand__name{font-size:34px;font-weight:700;color:var(--spine)}

  .cover-title{position:absolute;left:60px;top:480px;width:400px;font-size:21px;line-height:29px;font-weight:700;color:var(--accent)}
  .cover-lead{position:absolute;left:64px;top:546px;font-size:11.5px;line-height:18px;letter-spacing:-.15px;color:var(--ink-dark)}
  .cover-lead span{display:block;white-space:nowrap}
  .cover-lead span:first-child{font-size:12.5px;letter-spacing:0}
  .cover-questions{position:absolute;left:50px;top:590px;width:400px;list-style:none;font-size:11px;line-height:16px;color:var(--ink-dark)}
  .cover-questions li{position:relative;padding-left:18px}
  .cover-questions li::before{content:"";position:absolute;left:0;top:5px;width:6px;height:6px;background:var(--deep-red)}

  .section-title{position:absolute;left:34px;font-weight:900;color:var(--accent)}
  .section-text{position:absolute;left:34px;width:410px;font-size:10px;line-height:14px;font-weight:700;color:var(--ink-light)}
  .rule{position:absolute;left:36px;top:115px;width:400px;height:2px;background:var(--spine)}
  .benefits{list-style:none}

  .option-path{position:absolute;left:0;top:0}
  .option-num{position:absolute;width:28px;height:28px;border:1.5px solid var(--spine);border-radius:50%;
    font-family:"Dancing Script",cursive;font-size:20px;line-height:25px;text-align:center;color:var(--spine)}
  .option-label{position:absolute;font-family:"Dancing Script",cursive;font-size:23px;color:var(--accent)}
  .option-text{position:absolute;width:172px;font-size:10px;line-height:15.5px;font-weight:700;color:var(--ink-light)}
  .option-shot{position:absolute;border-radius:50%;background:#fff;border:2px solid #eee}
  .option-shot::after{content:"";position:absolute;left:37%;right:37%;top:14%;bottom:14%;border-radius:6px;
    background:linear-gradient(180deg,#222 0 12%,#f2f2f2 12% 88%,#222 88%)}
</style>
</head>
<body>

<section class="page page--front" aria-label="Portada">
  <svg class="cover-art" width="478" height="667" viewBox="0 0 478 667">
    <defs>
      <radialGradient id="photoTone" cx="0.6" cy="0.4" r="0.7">
        <stop offset="0" stop-color="var(--photo-light)"/>
        <stop offset="1" stop-color="var(--photo-blue)"/>
      </radialGradient>
    </defs>
    <circle cx="380" cy="150" r="322" fill="var(--deep-red)"/>
    <circle cx="380" cy="150" r="310" fill="url(#photoTone)" role="img" aria-label="Fotografía de oficina luminosa desenfocada"/>
  </svg>
  <div class="device-shot" role="img" aria-label="Teléfono móvil mostrando la pantalla de invitar amigos"></div>

  <div class="brand"><span class="brand__dot"></span><span class="brand__name">Brivolo</span></div>

  <h1 class="cover-title">Plataforma para la promoción y monetización de aplicaciones móviles</h1>
  <p class="cover-lead"><span>Actualmente, Latinoamérica representa una oportunidad de negocios</span><span>millonaria para los desarrolladores de juegos y aplicaciones móviles pero...</span></p>
  <ul class="cover-questions">
    <li>Cómo asegurarse de lograr monetizar una aplicación?</li>
    <li>Cómo construir una base significativa de usuarios leales en una zona donde la gran mayoría de los teléfonos móviles usan el sistema de prepago?</li>
  </ul>
</section>

<section class="page page--inside" aria-label="Página interior">
  <h2 class="section-title" style="top:14px;font-size:20px">SOLUCIÓN</h2>
  <p class="section-text" style="top:40px">Brivolo permite lograr el descubrimiento, promoción, instalación y monetización de juegos y aplicaciones móviles a través de una plataforma que integra varios modelos de descubrimiento, así como un motor de monetización y análisis avanzado.Obtención de usuarios leales y activos.Reducción de costos de adquisición de usuarios.Apoyo por un equipo de expertos en el mercado latinoamericano.</p>
  <div class="rule"></div>

  <h2 class="section-title" style="top:124px;font-size:18px">Beneficios</h2>
  <ul class="section-text benefits" style="top:151px">
    <li>Trabajamos con todas las plataformas</li>
    <li>Acceso web y móvil al dashboard</li>
    <li>Decisiones instruidas</li>
    <li>Herramientas de análisis avanzado y tablas de reportes.</li>
    <li>Integración simple a través de un sólo</li>
  </ul>

  <h2 class="section-title" style="top:224px;font-size:18px">LatAm</h2>
  <p class="section-text" style="top:250px">Somos pioneros en Latinoamérica en la creación de una plataforma sólida de descubrimiento móvil que toma en consideración todas las necesidades del desarrollador.</p>

  <svg class="option-path" width="475" height="667" viewBox="0 0 475 667">
    <path d="M206 306 C140 300 60 330 40 380" fill="none" stroke="var(--spine)" stroke-width="1.5" stroke-dasharray="6 5"/>
    <path d="M28 412 C10 470 30 560 150 620" fill="none" stroke="var(--spine)" stroke-width="1.5" stroke-dasharray="6 5"/>
  </svg>

  <span class="option-num" style="left:208px;top:290px">1</span>
  <span class="option-label" style="left:250px;top:288px">Opción</span>
  <p class="option-text" style="left:160px;top:324px">Compra de monedas: el usuario utiliza un sistema de facturación SMS premium.</p>
  <div class="option-shot" style="left:336px;top:303px;width:100px;height:100px" role="img" aria-label="Teléfono con pantalla de compra de monedas"></div>

  <span class="option-num" style="left:13px;top:370px">2</span>
  <span class="option-label" style="left:58px;top:368px">Opción</span>
  <div class="option-shot" style="left:16px;top:406px;width:104px;height:104px" role="img" aria-label="Teléfono con lista de amigos para invitar"></div>
  <p class="option-text" style="left:160px;top:414px">Obtención de monedas a cambio de invitación a amigos: el usuario puede obtener monedas virtuales por invitar a sus amigos a descargar el juego o aplicación móvil.</p>

  <span class="option-num" style="left:256px;top:515px">3</span>
  <span class="option-label" style="left:294px;top:513px">Opción</span>
  <div class="option-shot" style="left:136px;top:528px;width:106px;height:106px" role="img" aria-label="Teléfono con lista de amigos para invitar"></div>
  <p class="option-text" style="left:262px;top:552px">Obtención de monedas a cambio de invitación a amigos: el usuario puede obtener monedas virtuales por invitar a sus amigos a descargar el juego o aplicación móvil.</p>
</section>

</body>
</html>
```